Wine Label Design for a white wine made in the region of San Gimignano, Italy

This is a white wine (crisp and fresh) that is made in the region of San Gimignano, Italy, which is a beautiful hill town in Tuscany famous for it's towers. We would like a classy, elegant front wine label that can also be somewhat fun and whimsical if you prefer. Showcasing or depicting or alluding to the town and the towers of San Gimignano is a plus. The label should state the brand name which is "Vellisora", the varietal, which is Vernaccia di San Gimignano, and the vintage which is 2015. We might change the size of the label slightly but for design purposes please use 5 inches wide x 5 1/2 inches tall. I've uploaded a photo of a successful label design for parameters, but you should not feel limited to this either. Good white wine colors are white and green but we are flexible. Please don't use red, burgundy, or blue colors.

Target Market(s)

This wine label should appeal to all ages but be classy for the older crowd and still eye catching and fun for the millennials. This wine is sold in 15 states in the US, on the East Coast.

Industry/Entity Type

Town

Font styles to use
Serif
Sans Serif

Requirements
Must have
• Referring somehow or depicting the hill town and towers of San Gimignano in some way, such as in silhouette would be a plus. But also try to do something fun and unique with it-- not just an image of the town with words placed over it.
Should not have
• Please don't use the colors blue, reds. Try to think about what makes a wine label classy and sophisticated and 'upmarket' and what makes one cheap and cheesy. We are looking for the classy and sophisticated.

```html
<!DOCTYPE html>
<html lang="en">
<head>
<meta charset="utf-8">
<title>Vellisora – Vernaccia di San Gimignano 2015 label</title>
<link rel="stylesheet" href="https://fonts.googleapis.com/css2?family=Cormorant+Garamond:wght@500&family=EB+Garamond:wght@400&display=swap">
<style>
  :root {
    --page-bg: #f5f9ef;
    --label-bg: #f5f9ef;
    --brand-green: #4cb85a;
    --olive-text: #9a9062;
    --frame-green: #5cbf66;
    --hill-green: #4fb95b;
    --sand-light: #e6dca4;
    --sand-deep: #d2c150;
    --tower-brown: #8a6a40;
  }
  html, body {
    margin: 0;
    padding: 0;
    width: 1200px;
    height: 1055px;
    overflow: hidden;
    background: var(--page-bg);
  }
  .canvas {
    position: relative;
    width: 1200px;
    height: 1055px;
  }
  .wine-label {
    position: absolute;
    left: 122px;
    top: 77px;
    width: 956px;
    height: 900px;
    box-sizing: border-box;
    border: 2px solid var(--frame-green);
    background: var(--label-bg);
    overflow: hidden;
  }
  .brand-name {
    position: absolute;
    top: 150px;
    left: 0;
    right: 0;
    margin: 0;
    text-align: center;
    font-family: "Cormorant Garamond", serif;
    font-weight: 500;
    font-size: 100px;
    line-height: 1;
    font-variant: small-caps;
    letter-spacing: 0.09em;
    color: var(--brand-green);
  }
  .varietal {
    position: absolute;
    top: 262px;
    left: 0;
    right: 0;
    display: flex;
    justify-content: center;
    align-items: center;
    gap: 18px;
    font-family: "EB Garamond", serif;
    font-size: 38px;
    line-height: 1;
    color: var(--olive-text);
  }
  .varietal .rule {
    width: 72px;
    height: 2px;
    background: var(--olive-text);
  }
  .vintage {
    position: absolute;
    top: 405px;
    left: 0;
    right: 0;
    text-align: center;
    font-family: "Cormorant Garamond", serif;
    font-weight: 500;
    font-size: 62px;
    line-height: 1;
    letter-spacing: 0.06em;
    color: var(--olive-text);
    font-variant-numeric: oldstyle-nums;
  }
  .skyline {
    position: absolute;
    left: 0;
    bottom: 0;
    width: 100%;
    height: 340px;
    display: block;
  }
</style>
</head>
<body>
  <main class="canvas">
    <section class="wine-label">
      <h1 class="brand-name">Vellisora</h1>
      <p class="varietal"><span class="rule"></span>Vernaccia di San Gimignano<span class="rule"></span></p>
      <p class="vintage">2015</p>
      <svg class="skyline" viewBox="0 0 956 340" preserveAspectRatio="none" role="img" aria-label="Faceted low-poly illustration of the San Gimignano towers and green Tuscan hills in green, sand and brown tones">
        <defs>
          <linearGradient id="skylineTones" x1="0" y1="0" x2="0" y2="1">
            <stop offset="0" stop-color="#c9a46a"/>
            <stop offset="0.45" stop-color="#a9b865"/>
            <stop offset="0.7" stop-color="#e6dca4"/>
            <stop offset="1" stop-color="#d8c86a"/>
          </linearGradient>
        </defs>
        <rect x="0" y="0" width="956" height="340" fill="url(#skylineTones)"/>
      </svg>
    </section>
  </main>
</body>
</html>
```